Business Card Design

My business will be called TB Carpentry & Renovations. I am a liscenced carpentar who specialises in renovations/alterations/refurbishments and maintenance. I have experience in all types of Carpentry tho. I also have experience in tiling, painting and concrete which obviously gives me an edge in the refurbishment market for building. But i am not liscenced in these trades. I pride myself on being an honest and very reliable. There are alot of tradesman where i live who are not reliable so i really want to let the community know they can trust me and that i am willing to do all types of work.
I would like to see design and is not over the top but uses earthy/modern colours which presents a down to earth message.

I would really like to communicate diversity, reliabilty and quality work.

I have attached a couple of concepts i have come up with PrintNest, These may aid you.
Updates

Industry/Entity Type

Painting

Contact Information for Business Card

Name: Dean Holloway
Email: dean.holl@examplemail.net
Ph: 0418552916

Requirements
Must have
• Licence No: 581937K

```html
<!DOCTYPE html>
<html lang="en">
<head>
<meta charset="utf-8">
<title>TB Carpentry &amp; Renovations — Business Card</title>
<link rel="stylesheet" href="https://fonts.googleapis.com/css2?family=Oswald:wght@400&family=Poiret+One&display=swap">
<style>
  :root {
    --page: #ffffff;
    --cream: #f4eee0;
    --wood-light: #dcc1a6;
    --wood-mid: #cfae8f;
    --wood-dark: #c29f80;
    --ink: #1f1d1b;
    --rule-top: #8a3a14;
    --rule-bottom: #5a2410;
    --blade: #4a2a22;
    --screw-light: #d6dadb;
    --screw-dark: #5f6769;
    --edge: #b9b4a8;
  }
  * { box-sizing: border-box; margin: 0; padding: 0; }
  html, body {
    width: 1200px; height: 741px; overflow: hidden;
    background: var(--page);
  }
  .card {
    position: absolute; left: 43px; top: 41px;
    width: 1112px; height: 654px;
    background: var(--cream);
    border: 1px solid var(--edge);
    box-shadow: 0 1px 3px rgba(0,0,0,0.18);
  }
  .plank {
    position: absolute; left: 0; width: 100%;
    background: linear-gradient(180deg, var(--wood-light) 0%, var(--wood-mid) 55%, var(--wood-dark) 100%);
    box-shadow: 0 1px 2px rgba(0,0,0,0.2);
  }
  .plank--top { top: 0; height: 110px; }
  .plank--bottom { bottom: 0; height: 108px; }
  .screw {
    position: absolute; width: 44px; height: 44px; border-radius: 50%;
    background: radial-gradient(circle at 35% 35%, var(--screw-light), var(--screw-dark));
    box-shadow: 1px 2px 3px rgba(0,0,0,0.35);
  }
  .plank--top .screw { top: 33px; }
  .plank--bottom .screw { top: 32px; }
  .screw--left { left: 18px; }
  .screw--right { right: 18px; }
  .business-name {
    position: absolute; left: 90px; right: 90px; top: 10px;
    text-align: center; white-space: nowrap;
    font-family: "Oswald", sans-serif; font-weight: 400;
    font-size: 76px; line-height: 90px; letter-spacing: 0;
    color: var(--ink);
    text-shadow: 0 1px 0 rgba(255,255,255,0.25);
  }
  .identity {
    position: absolute; left: 0; right: 0; top: 180px;
    text-align: center; color: var(--ink);
    font-family: "Poiret One", sans-serif;
  }
  .identity__name {
    font-size: 60px; line-height: 72px;
    font-variant: small-caps; letter-spacing: 2px;
    color: var(--ink);
  }
  .identity__role {
    font-size: 30px; line-height: 36px; letter-spacing: 3px; margin-top: 2px;
    color: var(--ink);
  }
  .identity__licence {
    font-size: 34px; line-height: 44px; letter-spacing: 1px; margin-top: 4px;
    color: var(--ink);
  }
  .saw-blade {
    position: absolute; left: 806px; top: 362px;
    width: 144px; height: 72px;
    border-radius: 72px 72px 0 0;
    background: var(--blade);
  }
  .rule {
    position: absolute; left: 6px; right: 8px; top: 434px; height: 7px;
    background: linear-gradient(180deg, var(--rule-top), var(--rule-bottom));
  }
  .phone {
    position: absolute; left: 0; right: 0; top: 462px;
    text-align: center;
    font-family: "Poiret One", sans-serif;
    font-size: 48px; line-height: 60px; letter-spacing: 1px;
    color: var(--ink);
  }
  .email {
    position: absolute; left: 0; right: 0; top: 27px;
    text-align: center;
    font-family: "Poiret One", sans-serif;
    font-size: 42px; line-height: 54px;
    color: var(--ink);
  }
</style>
</head>
<body>
  <div class="card">
    <header class="plank plank--top" role="img" aria-label="Wooden plank header with wood-grain texture">
      <span class="screw screw--left" aria-hidden="true"></span>
      <h1 class="business-name">TB CARPENTRY &amp; RENOVATIONS</h1>
      <span class="screw screw--right" aria-hidden="true"></span>
    </header>

    <section class="identity">
      <p class="identity__name">Dean Holloway</p>
      <p class="identity__role">LICENSED CARPENTER</p>
      <p class="identity__licence">Licence No: 581937K</p>
    </section>

    <div class="saw-blade" role="img" aria-label="Circular saw blade rising above the line"></div>
    <div class="rule"></div>

    <p class="phone">0418552916</p>

    <footer class="plank plank--bottom" role="img" aria-label="Wooden plank footer with wood-grain texture">
      <span class="screw screw--left" aria-hidden="true"></span>
      <p class="email">dean.holl@examplemail.net</p>
      <span class="screw screw--right" aria-hidden="true"></span>
    </footer>
  </div>
</body>
</html>
```